Modern and Clean Web Re-Design Project

We have 2 companies in similar industries: Printing and Mail Preparation/Fulfillment. We prefer sites that are clean and easy to navigate.Our printing company, Harbourline Press Works' website, hpwdirect.example is outdated needs revamping. We have rebranded our logo and are looking for a new design that is clean, modern and geared to other corporations and business in the downtown Toronto area. Our mailing company, The Postwick Depot (thepostwickdepot.example) needs a website as well. This company is in the Direct Mail and letter shop business, which essentially is addressing/personalizing people's printed matter and preparing it for either the Canadian or US postal service. The Postwick Depot specializes in not-for-profit and corporate sectors.Please see our logos to get an idea of the colors and look we want. For all intensive purposes, the sites can look similar in design all we want is that each site has the appropriate corporate colors and is a bit different so they don't look identical as the two business run as separate corporations.The content of the website should be easily changed by our staff and we want it to be setup to optimized for SEO based on the keywords we want. We are looking for someone to work on this project immediately
Updates

Project Deadline Extended
Reason: Change of ideas

After doing some thinking, I would like the site to be more modern but the non flash sites that I have seen so far Im finding life-less and while I want something clean, not overly busy and corporate looking, I dont want the design to be bland looking.

Please design with the previous specs in mind but with a twist as mentioned above.

Thanks
Dorian

Target Market(s)

See above

Industry/Entity Type

Printing

Requirements
Must have
• Must match the design and style of each respective logoSee the attached impage of the front of our offices to have an idea of our lookWe must be able to edit the content ourselves without any fancy programs or tools.Must be SEO optimized
Nice to have
• An online order form that can be emailed to us for quotes.....perhaps a page with a bunch of fields that have drop down menus....
Should not have
• Should not be overly busy. I want it to be clean and simple but informative without being hard to navigate

```html
<!DOCTYPE html>
<html lang="en">
<head>
<meta charset="utf-8">
<title>Harbourline Press Works</title>
<link rel="stylesheet" href="https://fonts.googleapis.com/css2?family=Montserrat:wght@300;400;500;600&family=Oswald:wght@500&display=swap">
<style>
:root{
  --ink:#2b2a29;
  --orange:#f7a521;
  --orange-deep:#f0772c;
  --tan:#a57d58;
  --navy:#0f2537;
  --lime:#8cc63f;
  --peach:#fcefe4;
  --body:#5a5a5a;
  --rule:#d8d2cc;
  --white:#ffffff;
}
*{box-sizing:border-box;margin:0;padding:0}
html,body{width:1021px;height:1200px;overflow:hidden}
body{position:relative;background:var(--white);font-family:"Montserrat",sans-serif;color:var(--body)}
.abs{position:absolute;white-space:nowrap}
.site-header{left:0;top:0;width:1021px;height:410px;
  background:
   radial-gradient(ellipse 170px 150px at 0 290px,rgba(255,214,40,.95),rgba(240,130,30,.6) 55%,transparent 100%),
   radial-gradient(ellipse 170px 150px at 1021px 290px,rgba(255,214,40,.95),rgba(240,130,30,.6) 55%,transparent 100%),
   linear-gradient(#2a2928,#3a3837);}
.brand{left:136px;top:50px;display:flex;align-items:center;gap:12px;color:var(--orange);font-size:21px;font-weight:500;letter-spacing:.4px}
.brand-dot{width:30px;height:30px;border-radius:50%;background:var(--orange-deep)}
.head-phone{right:136px;top:26px;display:flex;align-items:center;gap:8px;color:var(--orange);font-size:20px;font-weight:500}
.head-mail{right:136px;top:52px;color:var(--white);font-size:11px}
.main-nav{right:136px;top:88px;display:flex;gap:27px}
.main-nav a{color:var(--white);font-size:13.5px;text-decoration:none;padding-bottom:7px}
.main-nav a.current{color:var(--orange);border-bottom:2px solid var(--orange)}
.slider{left:135px;top:136px;width:751px;height:331px;background:var(--white);padding:8px;box-shadow:0 6px 12px rgba(0,0,0,.15)}
.slide{width:100%;height:100%;background:linear-gradient(100deg,#b9b6b1 0%,#8f8a84 35%,#4c6e96 70%,#c7cacd 100%)}
.pager{left:472px;top:466px;display:flex;gap:3px}
.pager span{width:13px;height:17px;background:#d9d9d9;color:#fff;font-size:10px;text-align:center;line-height:15px}
.pager span.on{background:#2b2a29}
h2{font-weight:400;color:var(--ink);font-size:20px}
.mission{left:134px;top:535px;width:220px;white-space:normal}
.mission p{margin-top:14px;font-size:11.6px;line-height:16.6px;padding-left:2px}
.faq{left:402px;top:535px}
.faq ul{list-style:none;margin-top:16px}
.faq li{font-size:11.4px;color:var(--ink);margin-bottom:12.9px}
.faq li::before{content:"→";font-size:9px;margin-right:6px}
.depot{left:666px;top:529px;width:219px;height:228px;background:var(--navy);color:var(--white)}
.depot-name{position:absolute;left:22px;top:68px;font-size:17px;font-weight:600;color:var(--white);white-space:nowrap}
.depot-line{position:absolute;left:22px;display:flex;align-items:center;gap:10px;font-size:20px}
.band-title{left:135px;top:781px;font-size:22px;line-height:24px;font-weight:600;color:var(--ink);letter-spacing:.3px}
.service-bar{left:135px;top:807px;width:750px;height:51px;background:#262322;display:flex;align-items:center;justify-content:space-around;padding:0 4px}
.service-bar span{color:var(--orange);font-size:16px;letter-spacing:.4px;white-space:nowrap}
.contact-band{left:0;top:901px;width:1021px;height:90px;background:var(--peach)}
.tab{background:var(--orange);color:var(--white);font-size:13.5px;padding:5px 8px;border-radius:3px 3px 0 0;height:28px}
.contact-item{top:928px;display:flex;align-items:center;gap:9px;color:var(--ink)}
.contact-item small{display:block;font-size:11px}
.contact-item b{display:block;font-weight:500;font-size:14px}
.divider{top:927px;width:1px;height:44px;background:var(--rule)}
.social{top:939px;display:flex;align-items:center;gap:8px;font-size:13px;color:var(--ink)}
.social i{width:26px;height:26px;border-radius:3px;display:block;flex:none}
.foot-col{top:1003px}
.foot-col h3{font-weight:400;font-size:13px;color:var(--tan);margin-bottom:17px}
.foot-col li{list-style:none;font-size:11px;line-height:18.4px}
.join{left:540px;top:1005px;width:175px}
.join-title{background:var(--orange);color:var(--white);font-family:"Oswald",sans-serif;font-size:17px;padding:1px 6px;letter-spacing:.3px}
.join p{font-size:10.4px;color:var(--ink);margin:6px 0 0 2px;line-height:13px}
.join-field{margin-top:11px;position:relative;width:173px;height:21px;border:1px solid #c9c9c9;border-radius:11px;font-size:9.5px;padding:4px 9px;color:#666}
.join-field span{position:absolute;right:-2px;top:-1px;width:32px;height:21px;border-radius:11px;background:var(--orange-deep);color:#fff;font-family:"Oswald",sans-serif;font-size:10px;text-align:center;line-height:21px}
.address{left:733px;top:1007px;display:flex;gap:12px;color:var(--tan);font-size:13px;line-height:17px}
.foot-rule{left:119px;top:1154px;width:782px;height:1px;background:var(--rule)}
.copyright{left:0;top:1170px;width:1021px;text-align:center;font-size:10.5px}
</style>
</head>
<body>
<header class="site-header abs">
  <div class="brand abs"><span class="brand-dot"></span>Harbourline Press Works</div>
  <div class="head-phone abs">
    <svg width="26" height="26" viewBox="0 0 26 26"><circle cx="13" cy="13" r="12" fill="none" stroke="#a57d58" stroke-width="1.5"/><path d="M9 7l3 3-2 2c1 2 2 3 4 4l2-2 3 3-2 2c-5 0-10-5-10-10z" fill="#a57d58"/></svg>
    416-555-0142
  </div>
  <div class="head-mail abs">info@hpwdirect.example</div>
  <nav class="main-nav abs">
    <a class="current">Home</a><a>Who are we</a><a>What do we do</a><a>Email a file</a><a>Contact Us</a>
  </nav>
</header>

<div class="slider abs"><div class="slide" role="img" aria-label="Photo of two press operators working at a printing machine"></div></div>
<div class="pager abs"><span class="on">1</span><span>2</span><span>3</span><span>4</span><span>5</span></div>

<section class="mission abs">
  <h2>Mission Statement</h2>
  <p>We maintain absolute integrity in every aspect of our operation. By using our experience to understand our customers' expectations, we show an uncommon commitment to achieving a high-quality product under strict deadlines. It is the customers who set the standards we strive to achieve. We are professionals who bring unique and specialized skills you can depend on.</p>
</section>

<section class="faq abs">
  <h2>Commercial Printing</h2>
  <ul>
    <li>What is it used for?</li>
    <li>How long does an order take?</li>
    <li>Where is it done?</li>
    <li>Whom should I speak to?</li>
    <li>What do I need to know?</li>
    <li>How do I arrange for delivery?</li>
  </ul>
</section>

<aside class="depot abs">
  <div class="depot-name">The Postwick Depot</div>
  <div class="depot-line" style="top:123px">
    <svg width="26" height="26" viewBox="0 0 26 26"><circle cx="13" cy="13" r="12" fill="none" stroke="#8cc63f" stroke-width="1.5"/><path d="M9 7l3 3-2 2c1 2 2 3 4 4l2-2 3 3-2 2c-5 0-10-5-10-10z" fill="#8cc63f"/></svg>
    416-555-0170
  </div>
  <div class="depot-line" style="top:166px">
    <svg width="26" height="26" viewBox="0 0 26 26"><rect x="7" y="3" width="12" height="7" fill="#8cc63f"/><rect x="3" y="10" width="20" height="10" rx="2" fill="#8cc63f"/><rect x="7" y="16" width="12" height="8" fill="#0f2537" stroke="#8cc63f" stroke-width="1.5"/></svg>
    416-555-0183
  </div>
</aside>

<h2 class="band-title abs">HARBOURLINE PRESS WORKS</h2>
<div class="service-bar abs">
  <span>• LEGAL COPY</span><span>• DIGITAL PRINTING</span><span>• OFFSET PRINTING</span><span>• MAILING</span><span>• FUL FILLMENT</span>
</div>

<div class="contact-band abs"></div>
<div class="tab abs" style="left:127px;top:888px">Contact Us</div>
<div class="tab abs" style="left:711px;top:888px">Stay Connected</div>

<div class="contact-item abs" style="left:131px">
  <svg width="30" height="32" viewBox="0 0 30 32"><path d="M6 4l6 6-3 4c2 4 5 7 9 9l4-3 6 6-4 4C13 30 2 19 2 8z" fill="#a57d58"/></svg>
  <div><small>Phone</small><b>416-555-0142</b></div>
</div>
<div class="divider abs" style="left:285px"></div>
<div class="contact-item abs" style="left:304px">
  <svg width="36" height="32" viewBox="0 0 36 32"><rect x="9" y="2" width="18" height="9" fill="#a57d58"/><rect x="2" y="11" width="32" height="13" rx="3" fill="#a57d58"/><rect x="9" y="18" width="18" height="12" fill="#fcefe4" stroke="#a57d58" stroke-width="2"/></svg>
  <div><small>Fax</small><b>416-555-0183</b></div>
</div>
<div class="divider abs" style="left:463px"></div>
<div class="contact-item abs" style="left:478px">
  <svg width="30" height="26" viewBox="0 0 30 26"><rect x="1" y="3" width="28" height="21" rx="3" fill="#a57d58"/><path d="M2 5l13 10 13-10" fill="none" stroke="#fcefe4" stroke-width="2"/></svg>
  <div><small>Email:</small><b>info@hpwdirect.example</b></div>
</div>
<div class="social abs" style="left:712px"><i style="background:#5bb8e6"></i>Chirpline</div>
<div class="social abs" style="left:818px"><i style="background:#3b5a99"></i>Facepage</div>

<div class="foot-col abs" style="left:121px">
  <h3>Who are we</h3>
  <ul><li>Mission statement</li><li>Hours of operation</li><li>Where are we located</li><li>Pick up &amp; delivery</li><li>Grow your business</li></ul>
</div>
<div class="foot-col abs" style="left:262px">
  <h3>What do we do</h3>
  <ul><li>Digital printing</li><li>Commercial printing</li><li>Leagal services</li><li>Mailing house</li><li>Computer services</li><li>Free pick up &amp; delivery</li></ul>
</div>
<div class="foot-col abs" style="left:406px">
  <h3>Email a file</h3>
  <ul><li>E-mail order form</li><li>How to prepare a file</li></ul>
</div>

<div class="join abs">
  <div class="join-title">JOIN OUR MAILING LIST</div>
  <p>Sign up for our e-mail list to<br>receive updates</p>
  <div class="join-field">Your e-mail address<span>JOIN</span></div>
</div>

<div class="address abs">
  <svg width="14" height="20" viewBox="0 0 14 20"><path d="M7 0a7 7 0 017 7c0 5-7 13-7 13S0 12 0 7a7 7 0 017-7z" fill="#a57d58"/><circle cx="7" cy="7" r="2.5" fill="#fff"/></svg>
  <div>48 Carrow st west,<br>Concourse level,<br>Toronto, On M5V 0A1</div>
</div>

<div class="foot-rule abs"></div>
<p class="copyright abs">Copyright © 2012 Harbourline Press Works. All rights reserved.</p>
</body>
</html>
```